Business Card Design

We are a new residential construction company.our team is made up of young highly skilled tradesman of the next generation of carpenters coming through with new skills and ideas.we chose the name meridian as it means strikingly different from the rest as this is what we plan to be and we would like to portray this in our business card.we like Bold lettering as we want to make a statement, also the use of colour would be great as we want to stand out from the usual plain construction cards and logos.
I have attached a logo sketch I did as a rough idea if you can tidy it up or improve on it would be good.
I have also attached the LBP logo please include this on the card small but still legible.
open to any colourschemes ideas.
thanks
(note)please delete the LBP#308617 off from the card details please.
Updates
Industry/Entity Type
Construction
Contact Information for Business Card
MERIDIAN CONSTRUCTION LIMITED
Director:Kai Pereira
Mobile :0217364801
Email:Meridian.Construction@examplemail.test
Address:48 Halvorsen place,Ashgrove park 2071,Auckland
LBP#BP308617
Look and feel
Each slider illustrates characteristics of the customer's brand and the style your logo design should communicate.

```html
<!DOCTYPE html>
<html lang="en">
<head>
<meta charset="utf-8">
<title>Meridian Construction – Business Card</title>
<link rel="stylesheet" href="https://fonts.googleapis.com/css2?family=Open+Sans:wght@400;600;700&display=swap">
<style>
  :root {
    --backdrop: #d9d6d1;
    --card-top: #1e1f21;
    --card-bottom: #070708;
    --brand-blue: #2b9ad6;
    --text-light: #e6e6e6;
    --text-muted: #c9c9c9;
    --badge-fill: #e9e9e9;
    --badge-ring: #bdbdbd;
  }
  * { box-sizing: border-box; margin: 0; padding: 0; }
  html, body {
    width: 1200px;
    height: 1023px;
    overflow: hidden;
    background: var(--backdrop);
    font-family: "Open Sans", Arial, sans-serif;
  }
  .stage {
    width: 1200px;
    height: 1023px;
    display: flex;
    align-items: center;
    justify-content: center;
  }
  .business-card {
    position: relative;
    width: 1000px;
    height: 572px;
    border-radius: 30px;
    background: linear-gradient(160deg, var(--card-top) 0%, var(--card-bottom) 70%);
    box-shadow: 0 18px 40px rgba(0,0,0,0.35);
    overflow: hidden;
  }
  .wordmark {
    position: absolute;
    top: 70px;
    right: 80px;
    text-align: right;
    color: var(--brand-blue);
    font-weight: 700;
    line-height: 1;
  }
  .wordmark-name {
    display: block;
    font-size: 108px;
    letter-spacing: 2px;
  }
  .wordmark-sub {
    display: block;
    margin-top: 10px;
    font-size: 46px;
    letter-spacing: 6px;
  }
  .lbp-badge {
    position: absolute;
    left: 70px;
    top: 200px;
    width: 150px;
    height: 150px;
  }
  .holder {
    position: absolute;
    left: 70px;
    bottom: 70px;
  }
  .holder-name {
    color: var(--brand-blue);
    font-size: 34px;
    font-weight: 600;
    letter-spacing: 1px;
  }
  .holder-role,
  .holder-company {
    color: var(--text-muted);
    font-size: 20px;
    letter-spacing: 1px;
    margin-top: 6px;
  }
  .divider {
    position: absolute;
    left: 520px;
    top: 330px;
    width: 2px;
    height: 170px;
    background: var(--brand-blue);
  }
  .contact {
    position: absolute;
    left: 550px;
    top: 330px;
    color: var(--text-light);
    font-size: 21px;
    line-height: 1.55;
  }
  .contact-line {
    display: flex;
    align-items: center;
    gap: 10px;
  }
  .contact-icon {
    width: 20px;
    height: 20px;
    flex: none;
  }
</style>
</head>
<body>
<main class="stage">
  <section class="business-card" aria-label="Meridian Construction business card">
    <div class="wordmark">
      <span class="wordmark-name">MERIDIAN</span>
      <span class="wordmark-sub">CONSTRUCTION</span>
    </div>

    <svg class="lbp-badge" viewBox="0 0 150 150" role="img" aria-label="Licensed building practitioner badge">
      <circle cx="75" cy="75" r="72" fill="var(--badge-fill)"/>
      <circle cx="75" cy="75" r="50" fill="none" stroke="var(--badge-ring)" stroke-width="3"/>
    </svg>

    <div class="holder">
      <p class="holder-name">KAI PEREIRA</p>
      <p class="holder-role">DIRECTOR</p>
      <p class="holder-company">MERIDIAN CONSTRUCTION LIMITED</p>
    </div>

    <div class="divider"></div>

    <address class="contact" style="font-style:normal">
      <p class="contact-line">48 Halvorsen place,Ashgrove park 2071</p>
      <p class="contact-line">Auckland</p>
      <p class="contact-line">
        <svg class="contact-icon" viewBox="0 0 20 20" aria-hidden="true">
          <rect width="20" height="20" rx="3" fill="var(--brand-blue)"/>
          <path d="M6 4.5c-.8 0-1.5.8-1.3 1.8.6 4 4.9 8.4 9 9 1 .2 1.8-.5 1.8-1.3v-1.6l-2.8-1-1.2 1.3c-1.6-.7-2.8-1.9-3.5-3.5L9.3 8 8.3 4.5z" fill="#fff"/>
        </svg>
        0217364801
      </p>
      <p class="contact-line">
        <svg class="contact-icon" viewBox="0 0 20 20" aria-hidden="true">
          <rect width="20" height="20" rx="3" fill="var(--brand-blue)"/>
          <rect x="4" y="6" width="12" height="8.5" fill="none" stroke="#fff" stroke-width="1.5"/>
          <path d="M4 6l6 5 6-5" fill="none" stroke="#fff" stroke-width="1.5"/>
        </svg>
        Meridian.Construction@examplemail.test
      </p>
    </address>
  </section>
</main>
</body>
</html>
```